Website for Verdix Partners

We need to create a website for our company. Attached is the site map of the website and data input needed. Our theme colour is RED and our Logo is attached

We need a very attractive design where graphics are largely used like flash.

The main idea of the website is to show Telecommunications Suppliers World Wide that we could assist them in getting more business in Africa and Middle East through our local presence in this region.

Target Market(s)

Telecommunication Suppliers and Clients

Industry/Entity Type

Business

Font styles to use
Serif
Sans Serif

Colors
ec2027

Requirements
Must have
• Graphics that shows Telecommunications Suppliers World Wide that we could assist them in getting more business in Africa and Middle East through our local presence in this region.

The website should be easy to edit for future changes by us.
Nice to have
• New ideas

```html
<!DOCTYPE html>
<html lang="en">
<head>
<meta charset="utf-8">
<title>Verdix Partners</title>
<link href="https://fonts.googleapis.com/css2?family=Lato:ital,wght@0,300;0,400;0,700;0,900;1,400&family=Raleway:wght@400;600;700;800&family=Roboto+Mono:wght@300&display=swap" rel="stylesheet">
<style>
  :root{
    --red:#ec2027;
    --red-dark:#c4121a;
    --white:#ffffff;
    --ink:#222222;
    --grey-text:#555555;
    --soft-grey:#8a8a8a;
    --list-grey:#9a9a9a;
    --mint:#f4fbe8;
    --band:#9b9b9b;
    --link-blue:#1e6fb5;
    --social:#3b8fd0;
  }
  *{margin:0;padding:0;box-sizing:border-box}
  html,body{width:1200px;height:1200px;overflow:hidden;background:var(--white)}
  body{position:relative;font-family:"Lato",sans-serif;color:var(--ink)}
  .abs{position:absolute}

  .hero-photo{left:0;top:0;width:1200px;height:540px;
    background:radial-gradient(ellipse at 75% 35%,#d9b9a0 0%,#a67f66 30%,#4b3e39 65%,#2b2626 100%);}
  .hero-band{left:0;top:420px;width:1200px;height:115px;background:rgba(150,150,150,.72)}
  .mint-band{left:0;top:535px;width:1200px;height:123px;background:var(--mint)}

  .brand{left:254px;top:52px;font-family:"Roboto Mono",monospace;font-weight:300;font-size:19px;letter-spacing:2px;color:var(--white)}
  .main-nav{left:639px;top:52px;font-family:"Lato",sans-serif;font-weight:700;font-size:15px;color:var(--white);letter-spacing:-.3px}
  .main-nav span{margin:0 4px}
  .hero-title{left:255px;top:142px;font-family:"Lato",sans-serif;font-weight:900;font-size:48px;line-height:44px;letter-spacing:-2.5px;color:var(--white)}
  .hero-lead{left:265px;top:259px;width:420px;font-size:13px;line-height:14px;color:var(--white)}

  .service-card{top:403px;width:225px;height:147px;background:var(--white);box-shadow:0 4px 8px rgba(0,0,0,.35)}
  .card-image{position:absolute;left:3px;top:33px;width:219px;height:111px}
  .card-title{position:absolute;left:-3px;top:5px;width:228px;height:29px;background:linear-gradient(var(--red),var(--red-dark));
    font-family:"Raleway",sans-serif;font-weight:800;font-size:15px;color:var(--white);padding:5px 0 0 21px;letter-spacing:-.3px;box-shadow:0 2px 3px rgba(0,0,0,.3)}
  .read-more{position:absolute;left:142px;top:104px;width:89px;height:22px;background:linear-gradient(var(--red),var(--red-dark));
    font-family:"Lato",sans-serif;font-size:7px;color:var(--white);padding:6px 0 0 13px;box-shadow:0 2px 3px rgba(0,0,0,.3)}
  .read-more::after{content:"\27A4";position:absolute;right:12px;top:6px;font-size:7px}
  .card-text{top:577px;width:218px;font-family:"Raleway",sans-serif;font-size:9.5px;line-height:11.5px;color:var(--ink)}

  .intro-text{left:375px;top:711px;width:560px;font-family:"Raleway",sans-serif;font-size:14.5px;line-height:15px;color:var(--soft-grey)}
  .intro-label{left:379px;top:772px;font-size:14px;color:var(--ink)}
  .divider{left:100px;top:830px;width:1000px;height:8px;background:radial-gradient(ellipse at 50% 0%,rgba(0,0,0,.12),rgba(0,0,0,0) 70%)}

  .portfolio-heading{left:273px;top:909px;font-family:"Raleway",sans-serif;font-weight:700;font-size:12px;color:var(--soft-grey)}
  .portfolio-list{left:272px;top:947px;list-style:none;font-family:"Raleway",sans-serif;font-weight:700;font-size:12.5px;line-height:18px;color:var(--list-grey)}

  .quote-photo{left:633px;top:934px;width:72px;height:78px;background:var(--white);box-shadow:0 1px 4px rgba(0,0,0,.35);padding:4px}
  .quote-photo div{width:100%;height:100%;background:linear-gradient(160deg,#9fb6c9,#c7a894 55%,#5c86b0)}
  .quote-text{left:725px;top:939px;width:225px;font-style:italic;font-size:9.5px;line-height:13.5px;color:var(--grey-text)}
  .quote-author{left:637px;top:1031px;font-style:italic;font-size:10px;color:var(--link-blue)}
  .quote-company{left:642px;top:1044px;font-style:italic;font-size:7.5px;color:var(--ink)}
  .slider-dots{left:890px;top:1039px;display:flex;gap:3px}
  .slider-dots i{width:8px;height:8px;border-radius:50%;background:#dcdcdc}
  .slider-dots i:first-child{background:#b4b4b4}

  .footer-links{left:268px;top:1121px;font-size:9.5px;color:var(--ink);letter-spacing:-.3px}
  .copyright{left:268px;top:1136px;font-style:italic;font-size:7px;color:var(--grey-text)}
  .follow-label{left:832px;top:1122px;font-size:8px;color:var(--grey-text)}
  .social{top:1117px;width:17px;height:17px;border-radius:50%;background:var(--social);box-shadow:0 1px 2px rgba(0,0,0,.3)}
</style>
</head>
<body>
  <div class="abs hero-photo" role="img" aria-label="Photo of business people smiling around a laptop in an office"></div>
  <div class="abs hero-band"></div>
  <div class="abs mint-band"></div>

  <header>
    <div class="abs brand">VERDIX PARTNERS</div>
    <nav class="abs main-nav">HOME<span>|</span>PORTFOLIO<span>|</span>COMPANY<span>|</span>CONTACT</nav>
  </header>

  <h1 class="abs hero-title">YOUR CHALLENGE<br>IS OUR BUSINESS</h1>
  <p class="abs hero-lead">Verdix Partners is a leading telecommunication Solution Provider; the company provides state of the art technologies and turnkey solutions to its clients that fully support their business needs from planning right through full operation</p>

  <article class="abs service-card" style="left:247px">
    <div class="card-image" role="img" aria-label="Photo of a businessman drawing a chart line on glass" style="background:linear-gradient(120deg,#f1f4f6,#c9d3da 60%,#9aa6ae)"></div>
    <div class="card-title">Lorem Ipsum</div>
    <div class="read-more">READ MORE</div>
  </article>
  <article class="abs service-card" style="left:488px">
    <div class="card-image" role="img" aria-label="Photo of a smiling team around a laptop" style="background:linear-gradient(120deg,#e8ddd2,#b9a595 55%,#7f95ad)"></div>
    <div class="card-title">Consectetur Adipiscing</div>
    <div class="read-more">READ MORE</div>
  </article>
  <article class="abs service-card" style="left:729px">
    <div class="card-image" role="img" aria-label="Photo of a hand holding a tablet showing a newspaper" style="background:linear-gradient(120deg,#6b4a3a,#3a302c 40%,#c8ccd0 70%,#e8eaec)"></div>
    <div class="card-title">Elit Lorem</div>
    <div class="read-more">READ MORE</div>
  </article>

  <p class="abs card-text" style="left:258px;width:205px">Lorem ipsum dolor sit amet, consectetur adipisicing elit, sed do eiusmod tempor incididunt ut labore et dolore magna aliqua. Ut enim ad minim veniam, quis nostrud exercitation ullamco laboris nisi ut aliquip ex ea com-</p>
  <p class="abs card-text" style="left:494px">Lorem ipsum dolor sit amet, consectetur adipisicing elit, sed do eiusmod tempor incididunt ut labore et dolore magna aliqua. Ut enim ad minim veniam, quis nostrud exercitation ullamco laboris nisi ut aliquip ex ea commodo consequat.</p>
  <p class="abs card-text" style="left:740px">Lorem ipsum dolor sit amet, consectetur adipisicing elit, sed do eiusmod tempor incididunt ut labore et dolore magna aliqua. Ut enim ad minim veniam, quis nostrud exercitation ullamco laboris nisi ut aliquip ex ea commodo consequat.</p>

  <svg class="abs" style="left:268px;top:712px" width="56" height="52" viewBox="0 0 56 52" aria-hidden="true">
    <path d="M24 28 L24 6 A22 22 0 1 0 46 28 Z" fill="none" stroke="#8a8a8a" stroke-width="3"/>
    <path d="M24 28 L46 28 A22 22 0 0 1 8 43 Z" fill="#8a8a8a"/>
    <path d="M29 2 A20 20 0 0 1 49 20 L29 20 Z" fill="#8a8a8a"/>
    <rect x="33" y="6" width="20" height="2.5" fill="#fff"/>
    <rect x="36" y="12" width="18" height="2.5" fill="#fff"/>
    <rect x="40" y="23" width="14" height="2.5" fill="#8a8a8a"/>
  </svg>
  <p class="abs intro-text">Lorem ipsum dolor sit amet, consectetur adipisicing elit, sed do eiusmod tempor incididunt ut labore et dolore magna aliqua. Ut enim ad minim veniam, quis nostrud exercitation ullamco laboris nisi ut aliquip ex ea commodo consequat.</p>
  <p class="abs intro-label">Managed Services</p>
  <div class="abs divider"></div>

  <h2 class="abs portfolio-heading">PORTFOLIO</h2>
  <ul class="abs portfolio-list">
    <li>a. Access Network Solutions</li>
    <li>b. Transmission Network Solutions</li>
    <li>c. Core Network Solutions</li>
    <li>d. Value Added Services</li>
    <li>e. Managed Services</li>
    <li>f. Business Consultancy</li>
  </ul>

  <div class="abs quote-photo"><div role="img" aria-label="Portrait photo of a smiling senior client"></div></div>
  <p class="abs quote-text">Sed ut perspiciatis unde omnis iste natus sit voluptatem accusantium doloremque laudantium, totam rem aperiam, eaque ipsa quae ab illo inventore veritatis et quasi . Sed ut perspiciatis unde omnis iste natus sit voluptatem accusantium.</p>
  <p class="abs quote-author">- John Doe</p>
  <p class="abs quote-company">Company Name</p>
  <div class="abs slider-dots"><i></i><i></i><i></i></div>

  <footer>
    <p class="abs footer-links">Lorem | Ipsum Elit | Consectetur | Adipiscing | Lorem Ipsum</p>
    <p class="abs copyright">Copyright © 2014 Verdix-Partners. All Rights Reserved</p>
    <p class="abs follow-label">Folow us</p>
    <span class="abs social" style="left:878px"></span>
    <span class="abs social" style="left:899px"></span>
    <span class="abs social" style="left:920px;background:#2f5ea8"></span>
  </footer>
</body>
</html>
```